" Venda de planos de assistência familiar oferecendo uma rede descontos e funerais para os seus associados ; Serviços funerários; Venda de coroa de flores e arranjos. "

```html
<!DOCTYPE html>
<html lang="pt-BR">
<head>
<meta charset="UTF-8">
<title>Rede Amparo – Envelope</title>
<link rel="stylesheet" href="https://fonts.googleapis.com/css2?family=Montserrat:wght@400;500;700;800&display=swap">
<style>
  :root {
    --bg: #ecebe8;
    --paper: #ffffff;
    --paper-shade: #eef0f0;
    --aqua: #5cc9d1;
    --teal: #18897b;
    --teal-dark: #0f6f63;
    --teal-text: #2b8f86;
    --ink: #5a6a6a;
    --white: #ffffff;
  }
  * { box-sizing: border-box; margin: 0; padding: 0; }
  html, body { width: 1200px; height: 1200px; overflow: hidden; }
  body {
    background: var(--bg);
    font-family: "Montserrat", sans-serif;
    position: relative;
  }
  .envelope {
    position: absolute;
    left: 233px;
    width: 734px;
    height: 384px;
    overflow: hidden;
    box-shadow: 0 6px 18px rgba(0,0,0,.18);
  }
  /* back of envelope */
  .envelope-back { top: 185px; background: linear-gradient(180deg, var(--paper) 40%, var(--paper-shade)); }
  .envelope-back .flap { position: absolute; inset: 0; width: 100%; height: 150px; }
  .envelope-back .tree-watermark {
    position: absolute; right: 40px; top: 80px; width: 190px; height: 230px;
    background: radial-gradient(ellipse at center, rgba(150,160,160,.16), rgba(150,160,160,0) 70%);
  }
  .contact-strip {
    position: absolute; left: 36px; right: 36px; top: 300px;
    display: flex; align-items: center; gap: 30px;
    font-size: 9px; color: var(--ink); font-weight: 500;
  }
  .contact-item { display: flex; align-items: center; gap: 8px; line-height: 1.35; }
  .contact-item svg { width: 14px; height: 14px; flex: none; }
  .contact-item .dot { width: 12px; height: 12px; border: 1.6px solid var(--teal-text); border-radius: 50%; flex: none; }
  .base-band { position: absolute; left: 0; right: 0; bottom: 0; height: 34px; background: var(--paper-shade); }
  .base-band::before { content: ""; position: absolute; left: 0; right: 0; top: 0; height: 4px; background: var(--teal); }

  /* front of envelope */
  .envelope-front { top: 643px; background: linear-gradient(160deg, var(--teal) 0%, var(--teal-dark) 100%); }
  .brand { position: absolute; left: 72px; top: 120px; color: var(--white); }
  .brand-mark { width: 26px; height: 26px; border: 2px solid var(--white); border-radius: 50%; margin: 0 0 14px 62px; }
  .brand-name { font-size: 28px; font-weight: 800; letter-spacing: .5px; }
  .brand-tagline { font-size: 6.5px; font-weight: 500; letter-spacing: .8px; margin-top: 5px; opacity: .85; }
  .tree-art {
    position: absolute; right: 0; top: 0; width: 330px; height: 384px;
    background: radial-gradient(ellipse at 55% 40%, rgba(255,255,255,.22), rgba(92,201,209,.15) 45%, rgba(255,255,255,0) 75%);
  }
</style>
</head>
<body>
  <section class="envelope envelope-back">
    <svg class="flap" viewBox="0 0 734 150" preserveAspectRatio="none" aria-hidden="true">
      <polygon points="0,0 734,0 734,40 367,138 0,40" fill="var(--aqua)"/>
    </svg>
    <div class="tree-watermark" role="img" aria-label="Árvore decorativa em traço cinza claro"></div>
    <div class="contact-strip">
      <div class="contact-item">
        <svg viewBox="0 0 24 24"><path d="M6 3l3 4-2 2c1 3 4 6 7 7l2-2 4 3-2 3C10 20 4 14 3 5z" fill="var(--teal-text)"/></svg>
        <span>00 0000-0000 | 00 00000-0000</span>
      </div>
      <div class="contact-item">
        <svg viewBox="0 0 24 24"><rect x="3" y="6" width="18" height="12" rx="1" fill="none" stroke="var(--teal-text)" stroke-width="2"/><path d="M3 7l9 6 9-6" fill="none" stroke="var(--teal-text)" stroke-width="2"/></svg>
        <span>contato@redeamparo.com.br</span>
      </div>
      <div class="contact-item">
        <svg viewBox="0 0 24 24"><path d="M12 2a7 7 0 0 0-7 7c0 5 7 13 7 13s7-8 7-13a7 7 0 0 0-7-7z" fill="none" stroke="var(--teal-text)" stroke-width="2"/><circle cx="12" cy="9" r="2.5" fill="var(--teal-text)"/></svg>
        <span>Nome da Rua, 00 - Bairro<br>Cidade - Estado e CEP</span>
      </div>
      <div class="contact-item">
        <span class="dot"></span>
        <span>redeamparo</span>
      </div>
    </div>
    <div class="base-band"></div>
  </section>

  <section class="envelope envelope-front">
    <div class="brand">
      <div class="brand-mark"></div>
      <div class="brand-name">REDE AMPARO</div>
      <div class="brand-tagline">PLANO ASSISTENCIAL FAMILIAR COM DESCONTOS</div>
    </div>
    <div class="tree-art" role="img" aria-label="Ilustração de árvore estilizada em traços brancos e turquesa"></div>
  </section>
</body>
</html>
```